Junk Removal Website Design

We are working with a Junk Removal company in California. They provide junk hauling services for commercial and residential throughout California.
Some sites to use for inspiration:
https://www.1877binclear.com
https://haulwaycleanoutpro.com
https://www.quarrybrawnmovingclutter.com
https://www.clutterliftwardens.com
Thank you for taking the time to consider designing a website for us. We are web developers based in Stockton, CA, USA. Most of our projects go through the same process. Understanding this process may help you win a project with us. We custom-code all of our websites in-house. We don’t have any requirements as to what tools you use for your design, but we ask that you follow these guidelines.
IMAGES:
If you use any images or icons in the design, we ask that you have a link to the asset so we can purchase the image/icon. Most of the designs we submit do not have the customer’s images on them unless they have some great images. Be creative; show us the feeling you are trying to portray with your image choices. Use any royalty-free site you choose. We subscribe to Vexaro and mainly use their images, but we can purchase images outside of Vexaro. PLEASE NOTE: we will not submit designs to clients with watermarks on the images.
FONTS:
We ask that you identify the fonts you’re using in the design. This can be done in a message if you want. We typically use Plimbet Fonts and Vexaro Fonts.
CONTENT:
We're always open to different content and ideas. We often submit designs with stock images so the client can see our vision. We typically take pictures after the website launch to use their images with our vision. Lorem Ipsum is fine for paragraphs, but we ask that you make the Headers with correct English. We want to be able to show the vision and identify the sections of the website.
INSPIRATION:
We typically add a couple of links in the brief of websites we like to help you get started in your design.
REVISIONS:
We do not often ask for revisions of the designs unless we see something in the design that may not appeal to the client. If there are slight changes that we want to make, we do that in the development process.
FEEDBACK:
We rarely give feedback on designs during the design process. We are working on many website projects and do not have the time to provide feedback. We usually respond if your request is well thought out and asks specific questions, but a note asking “feedback, please” usually goes unanswered.
Number of Pages Required
1 page

```html
<!DOCTYPE html>
<html lang="en">
<head>
<meta charset="utf-8">
<title>Junk Removal</title>
<link href="https://fonts.googleapis.com/css2?family=Montserrat:ital,wght@0,400;0,500;0,600;0,700;0,800;0,900;1,400&family=Arimo:wght@400;700&display=swap" rel="stylesheet">
<style>
:root{
  --green:#55a544;
  --green-dark:#3f8a32;
  --black:#000;
  --ink:#111;
  --white:#fff;
  --grey:#6b6b6b;
  --star:#f39a12;
}
*{box-sizing:border-box;margin:0;padding:0}
html,body{width:1200px;height:4425px;overflow:hidden;background:var(--white)}
body{position:relative;font-family:'Arimo',Arial,sans-serif;color:var(--ink)}
.section{position:absolute;left:0;width:1200px}
.abs{position:absolute}
.head{font-family:'Montserrat',sans-serif;font-weight:900;text-transform:uppercase;line-height:1}
.eyebrow{font-family:'Montserrat',sans-serif;font-weight:800;font-size:21px;text-transform:uppercase;line-height:1}
.title{font-family:'Montserrat',sans-serif;font-weight:900;font-size:40px;text-transform:uppercase;line-height:1;color:var(--green)}
.center{left:0;width:1200px;text-align:center}
.btn{position:absolute;display:flex;align-items:center;justify-content:center;font-family:'Montserrat',sans-serif;font-weight:800;text-transform:uppercase;color:var(--white)}

/* header */
.site-header{top:0;height:129px;background:var(--white)}
.brand{position:absolute;display:flex;align-items:center;gap:10px}
.brand-dot{width:22px;height:22px;border-radius:50%;background:var(--green)}
.brand-name{font-family:'Montserrat',sans-serif;font-weight:900;font-size:32px;line-height:.95;text-transform:uppercase}
.site-header .brand-name{color:var(--black)}
.nav a{position:absolute;top:84px;font-family:'Montserrat',sans-serif;font-weight:700;font-size:15.5px;color:var(--ink);text-decoration:none;text-transform:uppercase}
.nav a.active{color:var(--green)}

/* hero */
.hero{top:129px;height:589px;background:linear-gradient(100deg,#3c4a33 0%,#56604e 30%,#5a5a5a 55%,#4e4e50 100%)}
.hero-title{left:615px;top:163px;font-size:50px;color:var(--white);letter-spacing:.5px}
.zip{left:615px;top:280px;width:446px;height:65px;background:var(--white);padding:6px}
.zip-field{position:absolute;left:14px;top:22px;font-family:'Montserrat',sans-serif;font-size:16px;color:#9a9a9a}
.zip .btn{right:7px;top:7px;width:222px;height:51px;background:var(--green);font-size:16px}
.hero-note{left:615px;top:369px;font-family:'Montserrat',sans-serif;font-weight:500;font-size:19px;color:var(--white)}

/* services */
.services{top:718px;height:632px}
.card{position:absolute;top:187px;width:236px;height:331px;color:var(--white);text-align:center}
.card.dark{background:var(--black)}
.card.light{background:var(--green)}
.card-photo{height:146px}
.card h3{margin-top:38px;font-family:'Montserrat',sans-serif;font-weight:800;font-size:16.5px;text-transform:uppercase}
.card p{margin:20px auto 0;width:170px;font-size:14px;line-height:18px}

/* about */
.about{top:1350px;height:455px;background:var(--black)}
.about-photo{left:550px;top:0;width:650px;height:455px;background:linear-gradient(90deg,#000 0%,#2e3a22 22%,#4c6a33 50%,#5b7a3c 75%,#6f8a52 100%)}
.about .eyebrow{left:129px;top:92px;color:var(--white)}
.about .title{left:129px;top:120px}
.about-copy{left:124px;top:161px;width:395px;color:var(--white);font-size:15.5px;line-height:23px}
.about .btn{left:127px;top:290px;width:144px;height:48px;background:var(--green);font-size:17px}

/* testimonials */
.testimonials{top:1805px;height:633px}
.review{position:absolute;top:250px;width:290px;height:284px;background:var(--white);box-shadow:0 2px 14px rgba(0,0,0,.09);padding:38px 36px}
.stars{display:flex;gap:10px}
.review p{margin-top:22px;font-family:'Montserrat',sans-serif;font-style:italic;font-size:14px;line-height:21.5px;color:var(--grey)}
.review .who{margin-top:20px;font-family:'Montserrat',sans-serif;font-weight:700;font-size:15px;color:var(--green)}

/* why */
.why{top:2438px;height:498px;background:var(--green);color:var(--white)}
.why .eyebrow{top:74px;color:var(--ink)}
.why .title{top:108px;color:var(--white)}
.divider{position:absolute;top:190px;width:1px;height:95px;background:rgba(255,255,255,.35)}
.feature{position:absolute;top:186px;width:250px;text-align:center}
.feature svg{display:block;margin:0 auto}
.feature p{margin-top:34px;font-family:'Montserrat',sans-serif;font-weight:600;font-size:17px;line-height:21px}

/* contact */
.contact{top:2936px;height:739px}
.contact .eyebrow{left:127px;top:146px}
.contact .title{left:127px;top:178px}
.contact-copy{left:125px;top:227px;width:305px;font-size:14.5px;line-height:18.5px;color:#333}
.info{position:absolute;left:127px;display:flex;gap:14px;align-items:flex-start;font-size:14.5px;line-height:18.5px;color:#333}
.info i{flex:none;width:30px;height:30px;border-radius:50%;background:var(--green);display:flex;align-items:center;justify-content:center}
.form{left:479px;top:129px;width:591px;height:505px;background:var(--black)}
.form label{position:absolute;color:var(--white);font-size:14.5px}
.form .field{position:absolute;background:var(--white);border:1px solid #ccc}
.form .btn{left:228px;top:415px;width:150px;height:48px;background:var(--green);font-size:18px}

/* cta */
.cta{top:3675px;height:326px;background:var(--green)}
.cta-title{top:94px;font-size:37px;color:var(--white);line-height:44px}
.cta .btn{left:469px;top:197px;width:262px;height:48px;background:var(--black);font-size:19px}

/* footer */
.site-footer{top:4001px;height:360px;background:var(--black);color:var(--white)}
.site-footer .brand-name{color:var(--white)}
.fcol h4{position:absolute;font-family:'Montserrat',sans-serif;font-weight:800;font-size:17px;text-transform:uppercase}
.fcol h4::after{content:"";display:block;width:40px;height:3px;background:var(--green);margin-top:5px}
.fcol ul{position:absolute;list-style:none;font-size:14px;line-height:23px;color:#d6d6d6}
.finfo{position:absolute;left:819px;display:flex;gap:14px;font-size:14px;line-height:18px;color:#d6d6d6}
.finfo i{flex:none;width:30px;height:30px;border-radius:50%;background:var(--green);display:flex;align-items:center;justify-content:center}
.copyright{top:4361px;height:64px;background:var(--green);color:var(--white);font-size:14.5px;display:flex;align-items:center;justify-content:center}
</style>
</head>
<body>

<header class="section site-header">
  <div class="brand" style="left:117px;top:32px">
    <span class="brand-dot"></span>
    <span class="brand-name">Junk<br>Removal</span>
  </div>
  <a class="btn" style="left:687px;top:17px;width:166px;height:38px;background:var(--black);font-size:15px;text-decoration:none">Free Estimate</a>
  <a class="btn" style="left:867px;top:17px;width:206px;height:38px;background:var(--green);font-size:15px;text-decoration:none">Schedule Removal</a>
  <nav class="nav">
    <a class="active" style="left:386px">Home</a>
    <a style="left:479px">About Us</a>
    <a style="left:611px">Services</a>
    <a style="left:735px">News</a>
    <a style="left:826px">Testimonials</a>
    <a style="left:992px">Contact</a>
  </nav>
</header>

<section class="section hero" role="img" aria-label="Crew in green uniforms loading boxes and bags into a green wheeled bin beside a collection truck">
  <h1 class="abs head hero-title">Welcome to<br>Junk Removal</h1>
  <div class="abs zip">
    <span class="zip-field">Enter Your ZIP Code</span>
    <span class="btn">Check Availability</span>
  </div>
  <p class="abs hero-note">No credit card required</p>
</section>

<section class="section services">
  <p class="abs eyebrow center" style="top:81px">What We Do</p>
  <h2 class="abs title center" style="top:103px">Our Services</h2>
  <article class="card dark" style="left:101px">
    <div class="card-photo" role="img" aria-label="Blue dumpster truck loaded with junk" style="background:linear-gradient(180deg,#7d8a8f,#2f4f86 60%,#3d3d3a)"></div>
    <h3>Service Name</h3>
    <p>Lorem ipsum dolor sit amet, consectetur adip iscing elied do eiusm od tempor incid.</p>
  </article>
  <article class="card light" style="left:354px">
    <div class="card-photo" role="img" aria-label="Worker in orange loading a green bin" style="background:linear-gradient(135deg,#3f8a32,#d9773a 55%,#3d6a2d)"></div>
    <h3>Service Name</h3>
    <p>Lorem ipsum dolor sit amet, consectetur adip iscing elied do eiusm od tempor incid.</p>
  </article>
  <article class="card dark" style="left:608px">
    <div class="card-photo" role="img" aria-label="Old wooden furniture stacked for removal" style="background:linear-gradient(135deg,#d9d2c3,#8a5a2f 50%,#4a3420)"></div>
    <h3>Service Name</h3>
    <p>Lorem ipsum dolor sit amet, consectetur adip iscing elied do eiusm od tempor incid.</p>
  </article>
  <article class="card light" style="left:860px">
    <div class="card-photo" role="img" aria-label="Green garbage collection truck" style="background:linear-gradient(135deg,#c9d3d8,#5fb83a 55%,#3e6e2a)"></div>
    <h3>Service Name</h3>
    <p>Lorem ipsum dolor sit amet, consectetur adip iscing elied do eiusm od tempor incid.</p>
  </article>
</section>

<section class="section about">
  <div class="abs about-photo" role="img" aria-label="Pile of rolled carpet, wood scraps and trash bags on a lawn"></div>
  <p class="abs eyebrow" style="left:129px;top:92px;color:var(--white)">Who We Are</p>
  <h2 class="abs title" style="left:129px;top:120px">About Us</h2>
  <p class="abs about-copy">Lorem ipsum dolor sit amet, consectetur adipiscing elit, sed do eiusmod tempor incididunt ut labore et dolore magna aliqua. Quis ipsum suspendisse ultrices gravida. Risus commodo viverra maecenas accumsan lacus vel facilisis.</p>
  <a class="btn">Read More</a>
</section>

<section class="section testimonials">
  <p class="abs eyebrow center" style="top:116px">Happy Clients</p>
  <h2 class="abs title center" style="top:138px">Client Testimonials</h2>
  <article class="review" style="left:127px">
    <div class="stars">
      <svg width="26" height="25" viewBox="0 0 24 23"><polygon fill="#f39a12" points="12,0 15,8 24,8.5 17,14 19.5,23 12,18 4.5,23 7,14 0,8.5 9,8"/></svg>
      <svg width="26" height="25" viewBox="0 0 24 23"><polygon fill="#f39a12" points="12,0 15,8 24,8.5 17,14 19.5,23 12,18 4.5,23 7,14 0,8.5 9,8"/></svg>
      <svg width="26" height="25" viewBox="0 0 24 23"><polygon fill="#f39a12" points="12,0 15,8 24,8.5 17,14 19.5,23 12,18 4.5,23 7,14 0,8.5 9,8"/></svg>
      <svg width="26" height="25" viewBox="0 0 24 23"><polygon fill="#f39a12" points="12,0 15,8 24,8.5 17,14 19.5,23 12,18 4.5,23 7,14 0,8.5 9,8"/></svg>
      <svg width="26" height="25" viewBox="0 0 24 23"><polygon fill="#f39a12" points="12,0 15,8 24,8.5 17,14 19.5,23 12,18 4.5,23 7,14 0,8.5 9,8"/></svg>
    </div>
    <p>Lorem ipsum dolor sit amet, consectetur adipiscing elit, sed do eiusmod tempor inci didunt ut labore et dololtre magna aliqua. Quis ipsum suspendisse ultrices.</p>
    <p class="who">Dario Venkel</p>
  </article>
  <article class="review" style="left:455px">
    <div class="stars">
      <svg width="26" height="25" viewBox="0 0 24 23"><polygon fill="#f39a12" points="12,0 15,8 24,8.5 17,14 19.5,23 12,18 4.5,23 7,14 0,8.5 9,8"/></svg>
      <svg width="26" height="25" viewBox="0 0 24 23"><polygon fill="#f39a12" points="12,0 15,8 24,8.5 17,14 19.5,23 12,18 4.5,23 7,14 0,8.5 9,8"/></svg>
      <svg width="26" height="25" viewBox="0 0 24 23"><polygon fill="#f39a12" points="12,0 15,8 24,8.5 17,14 19.5,23 12,18 4.5,23 7,14 0,8.5 9,8"/></svg>
      <svg width="26" height="25" viewBox="0 0 24 23"><polygon fill="#f39a12" points="12,0 15,8 24,8.5 17,14 19.5,23 12,18 4.5,23 7,14 0,8.5 9,8"/></svg>
      <svg width="26" height="25" viewBox="0 0 24 23"><polygon fill="#f39a12" points="12,0 15,8 24,8.5 17,14 19.5,23 12,18 4.5,23 7,14 0,8.5 9,8"/></svg>
    </div>
    <p>Lorem ipsum dolor sit amet, consectetur adipiscing elit, sed do eiusmod tempor inci didunt ut labore et dololtre magna aliqua. Quis ipsum suspendisse ultrices.</p>
    <p class="who">Dario Venkel</p>
  </article>
  <article class="review" style="left:778px">
    <div class="stars">
      <svg width="26" height="25" viewBox="0 0 24 23"><polygon fill="#f39a12" points="12,0 15,8 24,8.5 17,14 19.5,23 12,18 4.5,23 7,14 0,8.5 9,8"/></svg>
      <svg width="26" height="25" viewBox="0 0 24 23"><polygon fill="#f39a12" points="12,0 15,8 24,8.5 17,14 19.5,23 12,18 4.5,23 7,14 0,8.5 9,8"/></svg>
      <svg width="26" height="25" viewBox="0 0 24 23"><polygon fill="#f39a12" points="12,0 15,8 24,8.5 17,14 19.5,23 12,18 4.5,23 7,14 0,8.5 9,8"/></svg>
      <svg width="26" height="25" viewBox="0 0 24 23"><polygon fill="#f39a12" points="12,0 15,8 24,8.5 17,14 19.5,23 12,18 4.5,23 7,14 0,8.5 9,8"/></svg>
      <svg width="26" height="25" viewBox="0 0 24 23"><polygon fill="#f39a12" points="12,0 15,8 24,8.5 17,14 19.5,23 12,18 4.5,23 7,14 0,8.5 9,8"/></svg>
    </div>
    <p>Lorem ipsum dolor sit amet, consectetur adipiscing elit, sed do eiusmod tempor inci didunt ut labore et dololtre magna aliqua. Quis ipsum suspendisse ultrices.</p>
    <p class="who">Dario Venkel</p>
  </article>
</section>

<section class="section why">
  <p class="abs eyebrow center">Junk Removal</p>
  <h2 class="abs title center">Why Choose Us?</h2>
  <span class="divider" style="left:412px"></span>
  <span class="divider" style="left:781px"></span>
  <div class="feature" style="left:114px">
    <svg width="90" height="88" viewBox="0 0 90 88" fill="none" stroke="#fff" stroke-width="4" stroke-linecap="round">
      <path d="M72 22 A36 36 0 1 0 80 50"/><path d="M62 14 l12 6 -4 12"/>
      <path d="M44 24 v22 l-10 8"/>
      <circle cx="62" cy="78" r="2" fill="#fff"/><circle cx="72" cy="70" r="2" fill="#fff"/><circle cx="78" cy="60" r="2" fill="#fff"/>
    </svg>
    <p>We’ll be in and out in no time so you can get on with your day.</p>
  </div>
  <div class="feature" style="left:474px">
    <svg width="90" height="88" viewBox="0 0 90 88" fill="none" stroke="#fff" stroke-width="3" stroke-linecap="round" stroke-linejoin="round">
      <path d="M58 34 V12 H28 L14 26 V84 H58"/><path d="M28 12 V26 H14"/>
      <path d="M24 40 h4 M34 40 h16 M24 52 h4 M34 52 h14 M24 64 h4 M34 64 h10"/>
      <circle cx="66" cy="58" r="16"/><path d="M58 58 l6 6 10 -12"/>
    </svg>
    <p>Free onsite estimates with all-inclusive pricing. No hidden fees.</p>
  </div>
  <div class="feature" style="left:825px">
    <svg width="104" height="88" viewBox="0 0 104 88" fill="none" stroke="#fff" stroke-width="3" stroke-linejoin="round">
      <path d="M4 12 H64 V64 H4 Z"/><path d="M64 32 H84 L98 48 V64 H64"/>
      <path d="M70 38 H82 L90 48 H70 Z"/>
      <circle cx="22" cy="68" r="8" fill="#55a544"/><circle cx="82" cy="68" r="8" fill="#55a544"/>
      <path d="M12 24 h30 M12 34 h22"/>
    </svg>
    <p>We offer same-day service! We’re already on our way!</p>
  </div>
</section>

<section class="section contact">
  <p class="abs eyebrow">Get In Touch</p>
  <h2 class="abs title">Contact Us</h2>
  <p class="abs contact-copy">Lorem ipsum dolor sit amet, consectetur adipiscing elit, sed do eiusmod tempor incididunt ut labore et dolore magna aliqua. Quis ipsum suspendisse ultrices gravida. Risus commodo viverra maecenas accu msan lacus vel facilisis.</p>
  <div class="info" style="top:398px">
    <i><svg width="14" height="18" viewBox="0 0 14 18"><path fill="#fff" d="M7 0a7 7 0 0 1 7 7c0 5-7 11-7 11S0 12 0 7a7 7 0 0 1 7-7zm0 4a3 3 0 1 0 0 6 3 3 0 0 0 0-6z"/></svg></i>
    <span>Lorem Dum street 123 LJD<br>dumy numers 463.</span>
  </div>
  <div class="info" style="top:452px">
    <i><svg width="16" height="16" viewBox="0 0 16 16"><path fill="#fff" d="M3 0l3 4-2 2c1 2 4 5 6 6l2-2 4 3-2 3C7 16 0 9 0 2z"/></svg></i>
    <span>Phone:<br>123 456 7890</span>
  </div>
  <div class="info" style="top:505px">
    <i><svg width="16" height="12" viewBox="0 0 16 12"><path fill="#fff" d="M0 0h16v12H0z"/><path fill="none" stroke="#55a544" stroke-width="1.5" d="M0 1l8 6 8-6"/></svg></i>
    <span>Email:<br>info@company.com</span>
  </div>
  <form class="abs form">
    <label style="left:38px;top:45px">First Name</label>
    <span class="field" style="left:38px;top:58px;width:252px;height:45px"></span>
    <label style="left:306px;top:45px">Last Name</label>
    <span class="field" style="left:306px;top:58px;width:254px;height:45px"></span>
    <label style="left:38px;top:141px">Email</label>
    <span class="field" style="left:38px;top:154px;width:252px;height:45px"></span>
    <label style="left:306px;top:141px">Phone</label>
    <span class="field" style="left:306px;top:154px;width:254px;height:45px"></span>
    <label style="left:38px;top:228px">Zipcode</label>
    <span class="field" style="left:38px;top:242px;width:252px;height:43px"></span>
    <label style="left:306px;top:228px">Address</label>
    <span class="field" style="left:306px;top:242px;width:254px;height:43px"></span>
    <label style="left:38px;top:312px">Message</label>
    <span class="field" style="left:38px;top:326px;width:522px;height:100px"></span>
    <span class="btn">Submit</span>
  </form>
</section>

<section class="section cta">
  <h2 class="abs head center cta-title">Lorem ipsum dolor sit amet<br>consectetur adipiscing</h2>
  <a class="btn">Get a Free Quote</a>
</section>

<footer class="section site-footer">
  <div class="brand" style="left:132px;top:127px">
    <span class="brand-dot"></span>
    <span class="brand-name">Junk<br>Removal</span>
  </div>
  <div class="fcol">
    <h4 style="left:412px;top:64px">Menu</h4>
    <ul style="left:412px;top:100px">
      <li>Home</li><li>About Us</li><li>Services</li><li>Why Choose Us</li><li>Testimonials</li><li>Blog</li><li>Contact</li>
    </ul>
  </div>
  <div class="fcol">
    <h4 style="left:591px;top:64px">Links</h4>
    <ul style="left:591px;top:100px">
      <li>Pricing</li><li>FAQ</li><li>Book an Appointment</li><li>What We Do</li><li>What We Take</li><li>Business Services</li><li>No Contact Junk Removal</li><li>About Us</li>
    </ul>
  </div>
  <div class="fcol">
    <h4 style="left:819px;top:64px">Contact</h4>
  </div>
  <div class="finfo" style="top:112px">
    <i><svg width="14" height="18" viewBox="0 0 14 18"><path fill="#fff" d="M7 0a7 7 0 0 1 7 7c0 5-7 11-7 11S0 12 0 7a7 7 0 0 1 7-7zm0 4a3 3 0 1 0 0 6 3 3 0 0 0 0-6z"/></svg></i>
    <span>Lorem Dum street 123 LJD<br>dumy numers 463.</span>
  </div>
  <div class="finfo" style="top:166px">
    <i><svg width="16" height="16" viewBox="0 0 16 16"><path fill="#fff" d="M3 0l3 4-2 2c1 2 4 5 6 6l2-2 4 3-2 3C7 16 0 9 0 2z"/></svg></i>
    <span>Phone:<br>123 456 7890</span>
  </div>
  <div class="finfo" style="top:218px">
    <i><svg width="16" height="12" viewBox="0 0 16 12"><path fill="#fff" d="M0 0h16v12H0z"/><path fill="none" stroke="#55a544" stroke-width="1.5" d="M0 1l8 6 8-6"/></svg></i>
    <span>Email:<br>info@company.com</span>
  </div>
</footer>

<div class="section copyright">Copyright © 2023 Junk Removal. All Rights Reserved.</div>

</body>
</html>
```